Riverbend Haven Home Care-Nursing Assessment Form

I am creating a Nursing Assessment Form (which is used to be an intake form for all new patients) for my new home care company, Riverbend Haven Home Care.

It is 15 pages and pretty comprehensive as this is a very regulated field. I have all the necessary content and information attached in the word document below. Now, I am seeking a designer to make it look professional, cohesive and easy to read/ follow.
In order for your Word Document Design to be selected, you must:

1. As mentioned previously, make it easy to read/follow. There should be enough spacing, room to write out all necessary notes, fill out check marks...etc...
2. It should look professional.
3. It should be attractive and eye pleasing. Attached you will find our logo-kindly incorporate it's style into the project as well. The logo should be placed on top of each page.
4. Lastly, we need a Word Document version AND PDF Fillable Option. The fillable PDF should Auto Fill for the Name and Start of Care (SOC) Date.

I have attached a sample form below as well. This is how I envision the finished project to look. Of course, I am open to other suggestions as look as it meets the aforementioned requirements.

Thank you! May the best man or woman win!
Our team looks forward to working with our designer on this project!

Industry/Entity Type

Home Health Care

Font styles to use
Sans Serif

Colors
0255a3
9bcb3c

Requirements
Must have
• Refer to Project Description above.
Nice to have
We must be given a Word Document Option and PDF Fillable Option.

```html
<!DOCTYPE html>
<html lang="en">
<head>
<meta charset="utf-8">
<title>Riverbend Haven Home Care – Nursing Assessment Form</title>
<link href="https://fonts.googleapis.com/css2?family=Lato:wght@400;700&display=swap" rel="stylesheet">
<style>
:root{
  --blue:#0255a3;
  --green:#9bcb3c;
  --ink:#2b2b2b;
  --stage:#4a4b4d;
  --paper:#ffffff;
  --rule:#6a6a6a;
}
*{box-sizing:border-box;margin:0;padding:0}
html,body{width:1200px;height:1200px;overflow:hidden;background:var(--stage)}
body{font-family:'Lato',sans-serif;color:var(--ink)}
.stage{position:absolute;left:0;top:0;width:1500px;height:1500px;transform:scale(.8);transform-origin:0 0}
.page{position:absolute;background:var(--paper);overflow:hidden}
.page-one{left:101px;top:59px;width:482px;height:676px}
.page-two{left:869px;top:59px;width:484px;height:678px}
.page-three{left:500px;top:772px;width:490px;height:686px}

.brand{position:absolute;display:flex;align-items:center;gap:6px;color:var(--blue);font-weight:700;font-size:11px;line-height:1.15;white-space:nowrap}
.brand-dot{width:22px;height:22px;border-radius:50%;background:var(--green);flex:none}

.row{position:absolute;left:15px;right:14px;display:flex;align-items:center;gap:6px;font-size:9px;white-space:nowrap}
.box{border:1px solid var(--rule);height:13px;flex:1}
.box.fixed{flex:none}
.chk{display:inline-block;width:10px;height:10px;border:1px solid var(--rule);vertical-align:middle}
.line{border-bottom:1px solid var(--ink);flex:1;height:9px}
.spread{justify-content:space-between}

.section{position:absolute;left:0;right:0;display:flex;align-items:center;gap:8px;color:var(--blue);font-weight:700;font-size:14px}
.section::before,.section::after{content:"";height:1px;background:var(--green);flex:1}
.section.left-heavy::after{flex:.55}
.section.right-heavy::before{flex:.55}

.para{position:absolute;left:15px;right:14px;font-size:9px;line-height:14.2px}

.band-green{position:absolute;left:0;right:0;background:var(--green);color:var(--blue);font-weight:700;font-size:10px;display:flex;align-items:center}
.band-blue{position:absolute;left:0;right:0;bottom:0;background:var(--blue);color:#fff;font-size:9px}

.nutri-list{position:absolute;left:15px;top:360px;width:230px;font-size:8.6px;line-height:11.3px;list-style:none}
.nutri-list li{display:flex;gap:4px}
.nutri-list li span:first-child{width:12px;flex:none}
.values{position:absolute;left:245px;top:358px;font-size:9px;line-height:18.2px}
.score-key{position:absolute;left:289px;top:356px;width:175px;height:190px;background:var(--green);border:2px solid var(--blue);color:#fff;font-size:8.6px;line-height:11.3px;padding:25px 12px 0 16px}
.score-key p{margin-bottom:10px}
.subhead{position:absolute;color:var(--blue);font-weight:700;font-size:14px}

.adl{position:absolute;left:15px;top:118px;width:455px;border-collapse:collapse;font-size:8.6px}
.adl th{font-weight:400;text-align:left;padding:2px 2px 3px;border-bottom:1px solid var(--ink);white-space:nowrap}
.adl td{height:14.5px;padding:0 2px;border-bottom:1px solid var(--blue);line-height:1}
.adl th+th,.adl td+td{border-left:1.5px solid var(--blue)}
.comment-box{position:absolute;left:15px;top:296px;width:461px;height:52px;border:1px solid var(--rule)}
</style>
</head>
<body>
<div class="stage">

  <!-- Page one -->
  <section class="page page-one">
    <div class="brand" style="left:172px;top:28px"><span class="brand-dot"></span><span>Riverbend Haven<br>Home Care</span></div>

    <div class="row" style="top:101px"><span>Name :</span><span class="box fixed" style="width:226px"></span><span style="margin-left:16px">SOC :</span><span class="box"></span></div>
    <div class="row" style="top:124px;left:17px"><span>Patient'sName :</span><span class="box fixed" style="width:131px"></span><span style="margin-left:4px">Gender :</span><span class="box fixed" style="width:32px"></span><span>MR# :</span><span class="box fixed" style="width:32px"></span><span>Date:</span><span class="box"></span></div>
    <div class="row" style="top:146px"><span>Primary Diagnosis</span><span class="box fixed" style="width:131px"></span><span style="margin-left:5px">Secondary Diagnosis</span><span class="box"></span></div>
    <div class="row" style="top:171px"><span>Other Pertinent Diagnosis</span><span class="box fixed" style="width:104px"></span><span>PCPname</span><span class="box"></span></div>
    <div class="row" style="top:196px"><span>Prognosis :</span><span style="margin-left:8px;width:82px">( )Poor</span><span style="width:114px">( ) Fair</span><span style="width:120px">( )Good</span><span>( )Excellent</span></div>
    <div class="row" style="top:219px"><span>Vital Signs:</span><span>Height:</span><span class="box fixed" style="width:30px"></span><span>Weight:</span><span class="box fixed" style="width:30px"></span><span>Temp:</span><span class="box fixed" style="width:30px"></span><span>Pulse:</span><span class="box fixed" style="width:30px"></span><span>Resp:</span><span class="box fixed" style="width:30px"></span><span>B/P:</span><span class="box fixed" style="width:30px"></span></div>
    <div class="row" style="top:237px;right:22px"><span>Allergies :</span><span class="box"></span></div>
    <div class="row" style="top:256px;right:22px"><span>Past Medical and Surgical History :</span><span class="box"></span></div>

    <div class="section right-heavy" style="top:280px"><span>Support System</span></div>
    <div class="row" style="top:300px"><span>Married/Not Married/Single/Divorced/Widowed</span></div>
    <div class="row" style="top:319px"><span>Lives Alone :</span><span style="margin-left:4px">Yes</span><span class="chk"></span><span style="margin-left:4px">No</span><span class="chk"></span></div>
    <div class="row" style="top:338px"><span>Family Composition :</span><span class="box"></span></div>
    <div class="row" style="top:357px"><span>Legal Nextof Kin :</span><span class="box fixed" style="width:138px"></span><span>Telephone :</span><span class="box fixed" style="width:141px"></span></div>
    <div class="row" style="top:376px"><span>Address :</span><span class="box fixed" style="width:170px"></span><span>Email :</span><span class="box fixed" style="width:160px"></span></div>
    <div class="row" style="top:395px;left:18px"><span>Is significant other able, available, capable andwilling to care for patient?</span><span>Yes</span><span class="chk"></span><span style="margin-left:6px">No</span><span class="chk"></span></div>
    <div class="row" style="top:414px"><span>If No, explain</span><span class="box"></span></div>
    <div class="row" style="top:433px"><span>Educational Needs of Patient/Family</span><span class="box"></span></div>

    <div class="section" style="top:455px"><span>Environment</span></div>
    <div class="row spread" style="top:478px;right:20px"><span>( ) Private Home</span><span>( ) Apartment</span><span>( ) Elevator</span><span>( ) Walkup</span></div>

    <div class="section" style="top:501px"><span>Safety Hazards in the Home</span></div>
    <p class="para" style="top:521px">( ) Sound structure &nbsp;( ) Safe Placement of Cords, Rugs and Furniture &nbsp;( ) Adequate Heating and Ventilation &nbsp;( ) Adequate Cooking facility( ) Adequate Plumbing/Sanitation/ Running Water ( ) Adequate Sleeping Arrangement ( ) Safe Gas/Electric Appliances ( ) Grounded Plug for Equipment ( ) Enough Electrical Outlets for Equipment ( ) Working Telephone in the Home( ) Safe storage for Supplies/Equipment/Meds? () Exits Free of Obstruction ( ) Working smoke detectors? &nbsp;( ) Fire extinguisher in home?<br>( ) Infestations of pests? &nbsp;( ) Neighborhood safe?</p>

    <div class="band-green" style="top:613px;height:21px;justify-content:center">Caregiver's Contact Information :</div>
    <div class="band-blue" style="top:634px;display:flex;gap:0;padding:12px 0 0 18px;font-size:7px">
      <span style="width:78px">Name:</span><span style="width:96px">Telephone :</span><span style="width:88px">Address :</span><span style="width:76px">E-mail</span><span>Days /TimeAvailable:</span>
    </div>
  </section>

  <!-- Page two -->
  <section class="page page-two">
    <div class="brand" style="left:16px;top:30px"><span class="brand-dot"></span><span>Riverbend Haven<br>Home Care</span></div>
    <div class="row" style="top:33px;left:142px"><span>Name :</span><span class="box fixed" style="width:206px"></span><span>SOC :</span><span class="box"></span></div>

    <div class="row" style="top:89px;left:18px"><span>Caregiver has capacity to learn therapeutic regimen:</span><span style="margin-left:4px">( ) Yes</span><span style="margin-left:14px">( ) No</span></div>
    <div class="row" style="top:108px;left:18px"><span>Comments:</span><span class="box" style="height:12px"></span></div>
    <div class="row" style="top:126px;left:15px"><span>Are There Any Signs of Abuse or Neglect from Family or Caregiver?: ( ) Yes ( ) No</span></div>
    <div class="row" style="top:145px;left:15px;right:16px"><span>If Yes, describe:</span><span class="line" style="border-width:1.5px"></span></div>
    <div style="position:absolute;left:15px;right:16px;top:171px;border-top:1.5px solid var(--ink)"></div>

    <div class="section left-heavy" style="top:182px"><span>Advanced Directives</span></div>
    <div class="row" style="top:208px;left:15px"><span style="width:222px">Patient has a Living Will &nbsp; ( ) Yes &nbsp; ( ) No</span><span style="width:100px">Health Care Proxy</span><span>( ) Yes &nbsp; &nbsp; &nbsp; ( ) No</span></div>
    <div class="row" style="top:222px;left:15px"><span style="width:138px">Special Provisions Included :</span><span style="width:64px">( ) DNR</span><span style="width:54px">( ) DNI</span><span style="width:89px">( ) No Mech.</span><span>Ventilation ( )</span></div>
    <div class="row" style="top:236px;left:15px"><span>Med. Support Only &nbsp; ( ) No Feeding Tubes &nbsp; &nbsp; ( ) Copies of Documentation Attached &nbsp;( ) Yes &nbsp; &nbsp; ( ) No</span></div>
    <div class="row" style="top:251px;left:15px;right:19px"><span>Other :</span><span class="line" style="border-width:1.5px"></span></div>

    <div class="section left-heavy" style="top:271px"><span>Nutritional</span></div>
    <div class="row" style="top:298px;left:15px"><span>Diet:</span><span class="line fixed" style="flex:none;width:118px"></span><span style="margin-left:80px">Meals Prepared By:</span><span class="line fixed" style="flex:none;width:105px"></span></div>
    <div class="row" style="top:314px;left:15px"><span>Meals Patterns/Tolerance/Restrictions:</span><span class="line" style="flex:none;width:128px"></span><span style="margin-left:20px">Compliance: &nbsp;( ) Yes &nbsp; &nbsp; ( ) No</span></div>

    <div class="subhead" style="left:15px;top:338px">Statement</div>
    <div class="subhead" style="left:236px;top:338px">Value</div>
    <ol class="nutri-list">
      <li><span>1.</span><span>I have an illness or condition that made me change the kind and/or amount of food I eat</span></li>
      <li><span>2.</span><span>I eat fewer than two meals per day</span></li>
      <li><span>3.</span><span>I do not eat fruits, vegetables or milk products</span></li>
      <li><span>4.</span><span>I have three of more drinks of beer, liquor or wine almost every day</span></li>
      <li><span>5.</span><span>I have a tooth or mouth problems that make it hard for me to eat</span></li>
      <li><span>6.</span><span>I don't always have enough money to buy food</span></li>
      <li><span>7.</span><span>I eat alone most of the time</span></li>
      <li><span>8.</span><span>I have three or more different prescribed drugs or over-the counter drugs per day</span></li>
      <li><span>9.</span><span>Without wanting to, I have gained or lost ten pounds in the last six months</span></li>
      <li><span>10.</span><span>I am not always physically able to shop, cook or feed myself</span></li>
    </ol>
    <div class="values">2<br>3<br>2<br>2<br>2<br>4<br>1<br>1<br>2<br>2</div>
    <div class="row" style="top:548px;left:231px;right:auto"><span>Total:</span><span class="line" style="flex:none;width:26px"></span></div>
    <div class="score-key">
      <p>0-2: Low Nutritional Risks: Continue to evaluate Patient's nutritional needs and intervene as needed.</p>
      <p>3-5: Moderate Nutritional Risk: Educate patient/family/caregiver and improve Patient's eating habits and lifestyle.</p>
      <p>6+: High Nutritional Risk: Notify MD for further orders if indicated and consider special diet.</p>
    </div>

    <div class="row" style="top:574px;left:17px"><span style="width:75px">Exercise:</span><span style="width:139px">less than 1 hr week</span><span style="width:95px">2-5 hr per week</span><span>more than 6 hours per week</span></div>

    <div class="band-green" style="top:592px;height:22px;padding-left:18px">Immunizations/Screening Tests :</div>
    <div class="band-blue" style="top:614px;padding:7px 18px 0;line-height:11px">
      <div>Immunizations: &nbsp;Flu &nbsp;Yes __ &nbsp; &nbsp;No __ &nbsp; &nbsp; &nbsp; Date _____ &nbsp; &nbsp; &nbsp; &nbsp; &nbsp; &nbsp;Pneumonia &nbsp; Yes __ &nbsp; &nbsp; No __ &nbsp; &nbsp; Date _______</div>
      <div>Screening: Cholesterol level Yes __ &nbsp; No __ &nbsp; &nbsp; Date _____ &nbsp;Colon cancer screen &nbsp; Yes __ No __ Date _______</div>
      <div>Mammogram &nbsp; Yes __ No __ Date _____ &nbsp; Prostate cancer screen &nbsp; &nbsp; Yes __ No __ Date _______</div>
      <div>Pertinent Lab Results: ______________________________________</div>
    </div>
  </section>

  <!-- Page three -->
  <section class="page page-three">
    <div class="brand" style="left:17px;top:32px"><span class="brand-dot"></span><span>Riverbend Haven<br>Home Care</span></div>
    <div class="row" style="top:33px;left:144px"><span>Name :</span><span class="box fixed" style="width:206px"></span><span style="margin-left:4px">SOC :</span><span class="box"></span></div>

    <div class="subhead" style="left:15px;top:97px">Functional Level</div>
    <table class="adl">
      <tr><th style="width:75px">Activities of Daily</th><th style="width:60px">Unable to Do</th><th style="width:85px">Minimal Assistance</th><th style="width:92px">Moderate Assistance</th><th style="width:86px">Maximal Assistance</th><th>Independent</th></tr>
      <tr><td>Ambulation</td><td></td><td></td><td></td><td></td><td></td></tr>
      <tr><td>Stairs</td><td></td><td></td><td></td><td></td><td></td></tr>
      <tr><td>Dressing</td><td></td><td></td><td></td><td></td><td></td></tr>
      <tr><td>Feeding</td><td></td><td></td><td></td><td></td><td></td></tr>
      <tr><td>Household Tasks</td><td></td><td></td><td></td><td></td><td></td></tr>
      <tr><td>Transfer</td><td></td><td></td><td></td><td></td><td></td></tr>
      <tr><td style="height:22px">Self Care<br>(Groom./Bath)</td><td></td><td></td><td></td><td></td><td></td></tr>
      <tr><td style="border-bottom:none">Toileting</td><td style="border-bottom:none"></td><td style="border-bottom:none"></td><td style="border-bottom:none"></td><td style="border-bottom:none"></td><td style="border-bottom:none"></td></tr>
    </table>
    <div style="position:absolute;left:50px;right:20px;top:264px;border-top:1.5px solid var(--ink)"></div>

    <div class="section" style="top:274px"><span>Comments</span></div>
    <div class="comment-box"></div>

    <p class="para" style="top:358px;right:12px">Functional Limitations: ()Amputation &nbsp;( ) Bowel/Bladder Incontinence &nbsp;( ) Contracture &nbsp;( ) Hearing &nbsp;( ) Paralysis ( ) Endurance &nbsp;( ) Ambulation ( ) Speech ( ) Vision ( ) Poor Manual Dexterity ( ) Legally blind ( ) Dyspnea ( ) Poor Hand-Eye Coordination ( ) Unsteady Gait</p>
    <div class="row" style="top:402px;right:28px"><span>( ) Poor balance () Other:</span><span class="line"></span></div>
    <p class="para" style="top:421px;right:12px">Assistive Device: &nbsp;( ) Cane &nbsp; ( ) Quad cane &nbsp; ( ) Walker &nbsp; ( ) Rolling Walker &nbsp; ( ) Crutches &nbsp; ( ) Reg. Wheelchair &nbsp;( ) Electric Wheelchair</p>
    <div class="row" style="top:454px;right:36px"><span>() Other:</span><span class="box" style="height:11px"></span></div>
    <p class="para" style="top:474px;right:12px">Equipment: ( ) Hospital Bed &nbsp;( ) Commode &nbsp;( ) Hoyer lift &nbsp;( ) Nebulizer &nbsp;( ) Bath Chair &nbsp;( ) Apnea Machine ( )Oxygen Concentrator &nbsp; () &nbsp;Other:<br>( ) Ability of Patient/Family/Caregiver to Operate and Maintain Equipment at Home:</p>
    <div class="row" style="top:518px;right:15px"><span>Dural Medical Equipment Needed atHome:</span><span class="box" style="height:9px"></span></div>
    <p class="para" style="top:538px">Activities Permitted: &nbsp; ( ) Complete Bedrest &nbsp; ( ) Bedrest ( ) Up as tolerated ( ) Transfer bed to chair<br>( ) &nbsp;Independent in home</p>
    <div class="row" style="top:562px;right:22px"><span>() Other:</span><span class="box" style="height:9px"></span></div>
    <p class="para" style="top:578px">Risk Factors:<br>( ) Smoking &nbsp;( ) Obesity ( )Alcoholdependency ( )Drugabuse &nbsp;( ) None of the above</p>
    <div class="row" style="top:608px;right:28px"><span>( )Other:</span><span class="line"></span></div>

    <div class="band-green" style="top:626px;height:19px;padding-left:18px;font-size:10.5px;color:#1d3557">Cardiovascular</div>
    <div class="band-blue" style="top:645px;padding:6px 0 0 20px;font-size:8.4px">( ) Patient denies problems &nbsp; ( ) Chest pain &nbsp; ( ) Palpitations &nbsp; ( ) Vertigo &nbsp;( ) Syncope &nbsp;( ) Pulse deficit &nbsp;( ) PVD &nbsp;( ) Cyanosis</div>
  </section>

</div>
</body>
</html>
```